We require a business card that promotes our Electrical business. Things we would like included are;
1) our business name, Bright Path Electrical and Communication
2) Our Electrical licence, EC 27036
3) Our ABN, 52 147 906 318
4) Our website, www.ridgewirecrew.com.au
5) Our Email, info@ridgewirecrew.com.au
6) Our contact number, 0452 681 207
7) Our address, 48 Marlow Rd Tandridge Perth 6093
8) Our logo, I will attach this (can you please change it so the ackground is white not black)
9) Our colours are red and white and perhaps some black
10) Managing Director Dorian Velcourt
11) the back to say 'notes' and have some lines for writing

Target Market(s)

General

Industry/Entity Type

Electrical

Contact Information for Business Card

Include the colour white, black and red.

Font styles to use
Sans Serif

Requirements
Nice to have
• A thunder bolt or a power point or a cord or something electrical, cartoon image of a cartoon like electrical tradie

```html
<!DOCTYPE html>
<html lang="en">
<head>
<meta charset="utf-8">
<title>Bright Path Electrical and Communication – Business Card</title>
<link href="https://fonts.googleapis.com/css2?family=Open+Sans:wght@400;700&display=swap" rel="stylesheet">
<style>
  :root {
    --stage: #000000;
    --card: #ffffff;
    --red: #ec2027;
    --ink: #111111;
    --rule: #c9c9c9;
    --on-red: #ffffff;
  }
  * { margin: 0; padding: 0; box-sizing: border-box; }
  html, body { width: 1200px; height: 1200px; overflow: hidden; background: var(--stage); }
  body { font-family: "Open Sans", sans-serif; position: relative; }
  .card {
    position: absolute; left: 164px; width: 873px; height: 524px;
    background: var(--card); border-radius: 7px; overflow: hidden;
  }
  .card--front { top: 54px; }
  .card--back { top: 622px; }

  .brand-mark { position: absolute; border: 5px solid var(--red); border-radius: 50%; }
  .brand-name { position: absolute; color: var(--red); font-weight: 400; white-space: nowrap; }
  .company { position: absolute; color: var(--red); font-weight: 700; white-space: nowrap; }

  .card--front .brand-mark { left: 401px; top: 130px; width: 70px; height: 70px; }
  .card--front .brand-name { left: 0; width: 873px; text-align: center; top: 204px; font-size: 27px; }
  .card--front .company { left: 0; width: 873px; text-align: center; top: 282px; font-size: 24px; }

  .notes { position: absolute; left: 80px; right: 80px; top: 370px; }
  .notes__title { font-size: 18px; font-weight: 700; color: var(--red); line-height: 24px; }
  .notes__line { height: 1px; background: var(--rule); margin-top: 32px; }
  .notes__line:first-of-type { margin-top: 26px; }

  .card--back .company { left: 50px; top: 30px; font-size: 24px; }
  .abn { position: absolute; right: 31px; top: 30px; font-size: 20px; color: var(--ink); }
  .abn__label { color: var(--red); }
  .card--back .brand-mark { left: 52px; top: 148px; width: 72px; height: 72px; }
  .card--back .brand-name { left: 142px; top: 174px; font-size: 28px; }

  .director { position: absolute; left: 52px; top: 240px; white-space: nowrap; }
  .director__name { font-size: 20px; font-weight: 700; color: var(--ink); line-height: 26px; }
  .director__role { font-size: 16px; color: var(--red); line-height: 22px; }

  .contacts { position: absolute; left: 416px; top: 162px; list-style: none; }
  .contacts li {
    display: flex; align-items: center; height: 40px;
    font-size: 21px; color: var(--ink); white-space: nowrap;
  }
  .contacts svg { width: 13px; height: 13px; margin-right: 19px; fill: var(--red); flex: none; }

  .corner-swoosh { position: absolute; left: 0; top: 0; width: 873px; height: 524px; }
  .licence { position: absolute; left: 30px; top: 478px; font-size: 19px; color: var(--on-red); }
</style>
</head>
<body>
  <section class="card card--front">
    <span class="brand-mark"></span>
    <div class="brand-name">Ridgewirecrew</div>
    <div class="company">Bright Path Electrical and Communication</div>
    <div class="notes">
      <div class="notes__title">Notes</div>
      <div class="notes__line"></div>
      <div class="notes__line"></div>
      <div class="notes__line"></div>
    </div>
  </section>

  <section class="card card--back">
    <svg class="corner-swoosh" viewBox="0 0 873 524" aria-hidden="true">
      <path d="M0 326 Q230 332 336 524 L0 524 Z" fill="#ec2027"/>
    </svg>
    <div class="company">Bright Path Electrical and Communication</div>
    <div class="abn"><span class="abn__label">ABN : </span>52 147 906 318</div>
    <span class="brand-mark"></span>
    <div class="brand-name">Ridgewirecrew</div>
    <div class="director">
      <div class="director__name">Dorian Velcourt</div>
      <div class="director__role">Managing Director</div>
    </div>
    <ul class="contacts">
      <li><svg viewBox="0 0 16 16"><rect x="0" y="0" width="16" height="16" rx="3"/><path d="M5 3.5l2 2-1 1.3c.6 1.3 1.6 2.3 2.9 2.9l1.3-1 2 2-1.4 1.6C7.6 12 4 8.4 3.7 5z" fill="#fff"/></svg>0452 681 207</li>
      <li><svg viewBox="0 0 16 16"><path d="M0 3h16v1.5L8 9 0 4.5z"/><path d="M0 6.2l8 4.5 8-4.5V13H0z"/></svg>info@ridgewirecrew.com.au</li>
      <li><svg viewBox="0 0 16 16"><circle cx="8" cy="8" r="7.5"/><path d="M4 5c1.5 0 2.5 1 2 2.5S7 10 8 11M10 3c0 1.5 1.5 2 3 2" stroke="#fff" stroke-width="1.3" fill="none"/></svg>www.ridgewirecrew.com.au</li>
      <li><svg viewBox="0 0 16 16"><path d="M8 1L0 8h2.5v7h4v-4h3v4h4V8H16z"/></svg>48 Marlow Rd Tandridge Perth 6093</li>
    </ul>
    <div class="licence">Electrical licence, EC 27036</div>
  </section>
</body>
</html>
```